Business Card for Bright Meadow Lawn & Landscape

Double Sided Card Design - I think one side of the card should be cleaner, with logo, contact info, and "Complete Residential & Commercial Landscape Services", and on the other side it should list the services we offer:

- Lawn Care & Mowing
- Hedge & Shrub Trimming
- Leaf Removal & Clean Up
- Aeration & Sod
- Mulch & Rock Installations
- Landscape Installations & Renovations
- Commercial Snow Removal

Please make it clean and very professional... don't want it too be too busy, but want to tell them what we do.

Target Market(s)

Residential and Commercial

Industry/Entity Type

Landscape

Contact Information for Business Card

Fully Insured
Tom Berrigan
410-555-0198
Tberrigan07@mailbox-example.com

Requirements
Must have
• Double Sided, Cleaner on one side, more information and text on the other side.

```html
<!DOCTYPE html>
<html lang="en">
<head>
<meta charset="utf-8">
<title>Bright Meadow Lawn &amp; Landscape – Business Card</title>
<link rel="stylesheet" href="https://fonts.googleapis.com/css2?family=Cinzel:wght@400;600&family=Lato:wght@400&display=swap">
<style>
  :root {
    --backdrop: #3b3532;
    --card-black: #0d0d0d;
    --leaf-green: #86b840;
    --text-white: #ffffff;
    --text-soft: #e8e8e8;
    --divider-dark: #3a3a3a;
    --divider-light: rgba(255,255,255,0.55);
  }
  * { box-sizing: border-box; margin: 0; padding: 0; }
  html, body { width: 1200px; height: 900px; overflow: hidden; }
  body {
    background: var(--backdrop);
    display: flex;
    align-items: center;
    justify-content: center;
    gap: 40px;
    font-family: "Lato", Arial, sans-serif;
  }
  .card {
    width: 540px;
    height: 309px;
    position: relative;
    border-radius: 3px;
    box-shadow: 0 10px 30px rgba(0,0,0,0.45);
    overflow: hidden;
  }

  /* Contact side */
  .card--contact { background: var(--card-black); }
  .contact-brand {
    position: absolute; left: 30px; top: 60px; width: 200px;
    display: flex; flex-direction: column; align-items: center; gap: 14px;
  }
  .brand-dot {
    width: 70px; height: 70px; border-radius: 50%;
    background: var(--leaf-green);
  }
  .brand-name--contact {
    font-family: "Cinzel", Georgia, serif; font-weight: 600;
    color: var(--text-white); font-size: 17px; text-align: center; line-height: 1.25;
  }
  .contact-divider {
    position: absolute; left: 252px; top: 40px; width: 1px; height: 170px;
    background: var(--divider-dark);
  }
  .contact-details { position: absolute; left: 282px; top: 72px; }
  .person-name {
    font-family: "Cinzel", Georgia, serif; font-weight: 600;
    color: var(--leaf-green); font-size: 22px; margin-bottom: 26px;
  }
  .contact-line {
    display: flex; align-items: center; gap: 8px;
    color: var(--text-soft); font-size: 14px; margin-bottom: 8px;
  }
  .contact-line svg { width: 13px; height: 13px; flex: none; }
  .tagline {
    position: absolute; left: 0; right: 0; bottom: 30px; text-align: center;
    font-family: "Cinzel", Georgia, serif; color: var(--leaf-green);
    font-size: 14px; letter-spacing: 0.3px;
  }

  /* Services side */
  .card--services { background: var(--leaf-green); }
  .services-brand {
    position: absolute; left: 28px; top: 70px; width: 230px;
    display: flex; flex-direction: column; align-items: center; gap: 14px;
  }
  .brand-ring {
    width: 72px; height: 72px; border-radius: 50%;
    border: 6px solid var(--text-white);
  }
  .brand-name--services {
    font-family: "Cinzel", Georgia, serif; font-weight: 600;
    color: var(--text-white); font-size: 19px; text-align: center; line-height: 1.25;
  }
  .services-divider {
    position: absolute; left: 280px; top: 36px; width: 1px; height: 140px;
    background: var(--divider-light);
  }
  .service-list {
    position: absolute; left: 292px; top: 36px; list-style: none;
    color: var(--text-white); font-size: 13px; line-height: 20px;
  }
  .service-list li::before {
    content: ""; display: inline-block; width: 6px; height: 6px; border-radius: 50%;
    background: var(--text-white); margin-right: 6px; vertical-align: middle;
  }
  .insured {
    position: absolute; left: 310px; top: 212px;
    font-family: "Cinzel", Georgia, serif; font-weight: 600;
    color: var(--text-white); font-size: 19px; letter-spacing: 0.5px;
  }
</style>
</head>
<body>
  <section class="card card--contact">
    <div class="contact-brand">
      <span class="brand-dot"></span>
      <span class="brand-name--contact">Bright Meadow</span>
    </div>
    <div class="contact-divider"></div>
    <div class="contact-details">
      <p class="person-name">Tom Berrigan</p>
      <p class="contact-line">
        <svg viewBox="0 0 16 16" aria-hidden="true"><path fill="#86b840" d="M3.5 1.5l2.5 0 1 3.5-1.6 1.2a8 8 0 0 0 4.4 4.4L11 9l3.5 1v2.5c0 1-.8 1.5-1.8 1.5C7 14 2 9 2 3.3 2 2.3 2.5 1.5 3.5 1.5z"/></svg>
        410-555-0198
      </p>
      <p class="contact-line">
        <svg viewBox="0 0 16 16" aria-hidden="true"><rect x="1" y="3" width="14" height="10" rx="1" fill="#86b840"/><path d="M2 4l6 5 6-5" stroke="#0d0d0d" stroke-width="1.4" fill="none"/></svg>
        Tberrigan07@mailbox-example.com
      </p>
    </div>
    <p class="tagline">Complete Residential &amp; Commercial Landscape Services</p>
  </section>

  <section class="card card--services">
    <div class="services-brand">
      <span class="brand-ring"></span>
      <span class="brand-name--services">Bright Meadow Lawn &amp; Landscape</span>
    </div>
    <div class="services-divider"></div>
    <ul class="service-list">
      <li>Lawn Care &amp; Mowing</li>
      <li>Hedge &amp; Shrub Trimming</li>
      <li>Leaf Removal &amp; Clean Up</li>
      <li>Aeration &amp; Sod</li>
      <li>Mulch &amp; Rock Installations</li>
      <li>Landscape Installations &amp; Renovations</li>
      <li>Commercial Snow Removal</li>
    </ul>
    <p class="insured">Fully Insured</p>
  </section>
</body>
</html>
```